Copper lark buildworks

Copper lark buildworks is a small construction company.
Who is a licenced builder, Carpenter, joiner,
working on heritage ,new build, speacial projects and sometimes furniture

Industry/Entity Type

Construction

```html
<!DOCTYPE html>
<html lang="en">
<head>
<meta charset="utf-8">
<title>Copper lark buildworks – business card</title>
<link rel="stylesheet" href="https://fonts.googleapis.com/css2?family=Open+Sans:wght@400;600;700&display=swap">
<style>
  :root {
    --page-bg: #e9edf1;
    --card-paper: #f1f1ef;
    --brand-green: #8cc63f;
    --brand-green-text: #6cb33f;
    --deep-green: #0e7a3c;
    --pale-green: #cfe5b4;
    --band-white: #ffffff;
    --ink-grey: #4a4f52;
    --tagline-green: #11733a;
    --on-green: #ffffff;
  }
  * { box-sizing: border-box; margin: 0; padding: 0; }
  html, body { width: 1200px; height: 841px; overflow: hidden; }
  body {
    background: var(--page-bg);
    font-family: "Open Sans", Arial, sans-serif;
    position: relative;
  }
  .business-card {
    position: absolute;
    left: 100px; top: 130px;
    width: 1000px; height: 580px;
    background: var(--card-paper);
    overflow: hidden;
    box-shadow: 0 10px 30px rgba(0,0,0,.18);
  }
  .card-shapes { position: absolute; inset: 0; }
  .brand-name {
    position: absolute;
    left: 70px; top: 190px;
    font-size: 56px; font-weight: 700; line-height: 1.05;
    color: var(--brand-green-text);
  }
  .services {
    position: absolute;
    left: 70px; bottom: 50px; width: 420px;
    font-size: 21px; line-height: 1.3;
    color: var(--tagline-green);
  }
  .name-band {
    position: absolute;
    left: 585px; top: 150px;
    width: 390px; height: 100px;
    padding: 14px 0 0 60px;
  }
  .person-name {
    font-size: 40px; font-weight: 600; line-height: 1.05;
    color: var(--brand-green-text);
  }
  .person-role {
    font-size: 20px; font-weight: 600; letter-spacing: 5px;
    color: var(--ink-grey);
    padding-left: 14px;
  }
  .contact-list {
    position: absolute;
    left: 585px; top: 318px;
    list-style: none;
    color: var(--on-green);
    font-size: 22px; line-height: 1.25;
  }
  .contact-list li { display: flex; align-items: flex-start; gap: 14px; margin-bottom: 6px; }
  .contact-list svg { flex: none; width: 20px; height: 20px; margin-top: 4px; fill: var(--on-green); }
  .licence {
    position: absolute;
    right: 40px; top: 468px;
    font-size: 18px;
    color: var(--on-green);
  }
</style>
</head>
<body>
  <article class="business-card">
    <svg class="card-shapes" width="1000" height="580" viewBox="0 0 1000 580" aria-hidden="true">
      <polygon points="522,0 542,0 567,580 547,580" fill="var(--pale-green)"/>
      <polygon points="542,0 1000,0 1000,580 567,580" fill="var(--brand-green)"/>
      <line x1="543" y1="0" x2="568" y2="580" stroke="var(--deep-green)" stroke-width="5"/>
      <rect x="585" y="150" width="390" height="100" fill="var(--band-white)"/>
    </svg>

    <h1 class="brand-name">Copper lark<br>buildworks</h1>

    <p class="services">Carpenter, joiner,workingon heritage new build speacial projects and sometimes furniture</p>

    <div class="name-band">
      <p class="person-name">JOHN DOE</p>
      <p class="person-role">DIRECTOR</p>
    </div>

    <ul class="contact-list">
      <li>
        <svg viewBox="0 0 24 24"><path d="M6.6 10.8a15 15 0 0 0 6.6 6.6l2.2-2.2a1 1 0 0 1 1-.25 11.4 11.4 0 0 0 3.6.57 1 1 0 0 1 1 1V20a1 1 0 0 1-1 1A17 17 0 0 1 3 4a1 1 0 0 1 1-1h3.5a1 1 0 0 1 1 1c0 1.25.2 2.45.57 3.6a1 1 0 0 1-.25 1z"/></svg>
        <span>09 555 0142</span>
      </li>
      <li>
        <svg viewBox="0 0 24 24"><path d="M2 5h20v14H2z M3.5 6.5 12 13l8.5-6.5" fill="none" stroke="#fff" stroke-width="2"/></svg>
        <span>hello@copperlark.example</span>
      </li>
      <li>
        <svg viewBox="0 0 24 24"><path d="M12 3 2 12h3v9h5v-6h4v6h5v-9h3z"/></svg>
        <span>41 kowhai lane riverhead<br>auckland 0820</span>
      </li>
    </ul>

    <p class="licence">licenced builder</p>
  </article>
</body>
</html>
```